K Velmor Architectural Construction & Abatement, Inc.
K Velmor Architectural Construction, Inc.
Pilo 47:
86# Has very little orange. Use these colors please. Read all the reviews I gave other designers. Incorporate these ideas into to your design. Push forth these ideas.
Thank you,
rovatique:
Use more green color. Green on back of the card. And on stationary. Continue to push forth with these ideas.
Trulsen:
# 83 Remove the fax information on stationary
# 83 remove the black color on cards & Stationary. Use the original colors. Place motto on back as well.
Use little more green color on front. Green Energy feel. Use the orange as well. Put the logos on envelopes.
erovatique:
Please, include my education on the business cards. BArch, MArch. Thank You.
Pilo47:
Please, find away to include my education details on my business cards: BArch, MArch
I like some of the cards you have put together so far. And I have selected my favorites my star rating system. I asked that the front remain the same. But, the back have another logo which says K Velmor Architect ABATEMENT. I will upload the design for the business cards. Continue, to push the ideas.

```html
<!DOCTYPE html>
<html lang="en">
<head>
<meta charset="utf-8">
<title>K Velmor Architects – Business Card</title>
<link rel="stylesheet" href="https://fonts.googleapis.com/css2?family=PT+Sans:ital,wght@0,400;0,700;1,400;1,700&display=swap">
<style>
  :root {
    --bg: #e8e5e0;
    --card: #ffffff;
    --ink: #3a3a3a;
    --muted: #8a8a8a;
    --blue: #1d62a8;
    --green: #6cb33f;
    --orange: #f26a21;
    --rule: #b9b9b9;
  }
  html, body {
    margin: 0;
    width: 1200px;
    height: 780px;
    overflow: hidden;
    background: var(--bg);
    font-family: "PT Sans", sans-serif;
  }
  .canvas {
    position: relative;
    width: 1200px;
    height: 780px;
  }
  .business-card {
    position: absolute;
    left: 150px;
    top: 132px;
    width: 900px;
    height: 516px;
    background: var(--card);
    border-radius: 30px;
    box-shadow: 0 10px 28px rgba(0,0,0,0.18);
  }
  .brand {
    position: absolute;
    top: 112px;
    left: 0;
    width: 100%;
    display: flex;
    justify-content: center;
    align-items: center;
    gap: 22px;
  }
  .brand-mark {
    width: 74px;
    height: 74px;
    background: var(--orange);
  }
  .brand-name {
    font-weight: 700;
    font-size: 58px;
    line-height: 1;
    color: var(--blue);
    letter-spacing: 1px;
    text-transform: uppercase;
  }
  .identity {
    position: absolute;
    top: 268px;
    left: 0;
    width: 100%;
    margin: 0;
    text-align: center;
    font-size: 28px;
    line-height: 36px;
    white-space: nowrap;
  }
  .person-name {
    color: var(--blue);
    font-weight: 700;
  }
  .credentials {
    color: var(--blue);
    font-weight: 400;
    font-size: 22px;
  }
  .separator {
    color: var(--muted);
    margin: 0 10px;
  }
  .person-role {
    color: var(--green);
    font-style: italic;
    font-weight: 700;
    font-size: 24px;
  }
  .contact {
    position: absolute;
    top: 334px;
    left: 0;
    width: 100%;
    display: flex;
    justify-content: center;
    font-size: 22px;
    color: var(--ink);
    line-height: 36px;
  }
  .address {
    text-align: right;
    padding-right: 26px;
    border-right: 2px solid var(--rule);
  }
  .reach {
    padding-left: 26px;
  }
  .reach-row {
    display: flex;
    align-items: center;
    gap: 12px;
  }
  .reach-icon {
    width: 22px;
    height: 22px;
    flex: none;
  }
</style>
</head>
<body>
<main class="canvas">
  <article class="business-card">
    <header class="brand">
      <div class="brand-mark"></div>
      <div class="brand-name">K Velmor Architects</div>
    </header>

    <p class="identity">
      <span class="person-name">Marcus Hale</span><span class="credentials">, BArch, MArch</span><span class="separator">/</span><span class="person-role">Architect Intern / Project Manager</span>
    </p>

    <section class="contact">
      <div class="address">
        2390 FM 418 North<br>
        Harlow, Texas 77312
      </div>
      <div class="reach">
        <div class="reach-row">
          <svg class="reach-icon" viewBox="0 0 22 22" aria-hidden="true">
            <rect x="5" y="1" width="12" height="20" rx="2.5" fill="var(--blue)"/>
            <rect x="7.5" y="4" width="7" height="9" fill="#ffffff"/>
            <circle cx="11" cy="17" r="1.6" fill="#ffffff"/>
          </svg>
          <span>(555) 318-2704</span>
        </div>
        <div class="reach-row">
          <svg class="reach-icon" viewBox="0 0 22 22" aria-hidden="true">
            <text x="11" y="18" text-anchor="middle" font-family="PT Sans, sans-serif" font-weight="700" font-size="22" fill="var(--blue)">@</text>
          </svg>
          <span>kvelmorbuild@mailbox.com</span>
        </div>
      </div>
    </section>
  </article>
</main>
</body>
</html>
```